Business Card

Just need business logo with phone number on it. 0487 312 556
And the following on the bottom of the card.

"Your local plumbing experts".
and emblems for kelpa card, cheque and cash

```html
<!DOCTYPE html>
<html lang="en">
<head>
<meta charset="utf-8">
<title>Ridgeline Plumbing &amp; Drainage – Business Card</title>
<link href="https://fonts.googleapis.com/css2?family=Open+Sans:wght@400;600;700&display=swap" rel="stylesheet">
<style>
  :root {
    --backdrop: #e9e6e2;
    --card: #000000;
    --brand-red: #e3262f;
    --brand-blue: #1e9ad6;
    --text-light: #ffffff;
  }
  html, body {
    margin: 0;
    padding: 0;
    width: 1200px;
    height: 1000px;
    overflow: hidden;
    background: var(--backdrop);
  }
  .canvas {
    width: 1200px;
    height: 1000px;
    display: flex;
    align-items: center;
    justify-content: center;
  }
  .business-card {
    width: 999px;
    height: 597px;
    background: var(--card);
    box-sizing: border-box;
    display: flex;
    flex-direction: column;
    align-items: center;
    font-family: "Open Sans", sans-serif;
    color: var(--text-light);
    text-align: center;
  }
  .brand {
    margin-top: 118px;
    display: flex;
    align-items: center;
    gap: 18px;
  }
  .brand-dot {
    width: 44px;
    height: 44px;
    border-radius: 50%;
    background: var(--brand-blue);
  }
  .brand-name {
    font-weight: 700;
    font-size: 46px;
    line-height: 1.1;
    letter-spacing: 1px;
    color: var(--brand-red);
    text-transform: uppercase;
  }
  .brand-sub {
    display: block;
    font-size: 30px;
    letter-spacing: 4px;
  }
  .contact-name {
    margin: 62px 0 10px;
    font-weight: 700;
    font-size: 31px;
    color: var(--brand-red);
    letter-spacing: 0.5px;
  }
  .contact-line {
    margin: 0;
    font-size: 23px;
    line-height: 32px;
  }
  .tagline {
    margin: 20px 0 0;
    font-weight: 600;
    font-size: 23px;
    line-height: 32px;
  }
  .payment-note {
    margin: 0;
    font-size: 23px;
    line-height: 32px;
  }
</style>
</head>
<body>
  <main class="canvas">
    <section class="business-card">
      <div class="brand">
        <span class="brand-dot" aria-hidden="true"></span>
        <div class="brand-name">Ridgeline<span class="brand-sub">Plumbing &amp; Drainage</span></div>
      </div>
      <h1 class="contact-name">DANIEL MARSH</h1>
      <p class="contact-line">0487 312 556</p>
      <p class="contact-line">info@ridgelineplumbing.com.au</p>
      <p class="tagline">“Your local plumbing experts"</p>
      <p class="payment-note">Emblems for kelpa card, cheque and cash</p>
    </section>
  </main>
</body>
</html>
```